Coin collector banner ad for specialty insurance

We need a logo designed banner ad (multiple ads) to align with the coin collector market while incorporating color palette logo and call to action. Color palette of Kestrelby. Dimension, images, example designs and color palette attached. The context should include 'Specialty Insurance for your coin collection' please refer to the designed examples

Target Market(s)

Coin collectors 30-65+ years of age primarily male

Industry/Entity Type

Insurance

Font styles to use
Sans Serif

Requirements
Must have
• color palette, logo, word mark, Call to Action, The words 'Specialty Insurance for your coin collection'
Nice to have
• Call to actions
Should not have
• ba

```html
<!DOCTYPE html>
<html lang="en">
<head>
<meta charset="utf-8">
<title>Kestrelby – Specialty Insurance for Your Coin Collection</title>
<link rel="stylesheet" href="https://fonts.googleapis.com/css2?family=Oswald:wght@600&family=Montserrat:wght@400;500;700&display=swap">
<style>
  :root {
    --white: #ffffff;
    --ink: #1c1c1c;
    --blue-light: #22a6e2;
    --blue-mid: #1687d2;
    --blue-deep: #0b4fb0;
    --blue-navy: #0a3f98;
    --cta-shadow: #0b58b8;
    --gold-1: #f3d36b;
    --gold-2: #b8861c;
    --silver-1: #f4f4f4;
    --silver-2: #9a9ea4;
    --bronze-1: #5b4a36;
    --bronze-2: #1d1812;
  }
  * { margin: 0; padding: 0; box-sizing: border-box; }
  html, body { width: 1200px; height: 628px; overflow: hidden; background: var(--white); }
  .banner {
    position: relative;
    width: 1200px;
    height: 628px;
    overflow: hidden;
    background: var(--white);
    font-family: "Montserrat", Arial, sans-serif;
  }
  .backdrop { position: absolute; inset: 0; }
  .coins { position: absolute; left: 40px; top: 40px; width: 620px; height: 500px; }
  .brand {
    position: absolute;
    top: 40px;
    left: 822px;
    display: flex;
    align-items: center;
    gap: 18px;
  }
  .brand-name {
    font-weight: 700;
    font-size: 33px;
    letter-spacing: 1px;
    color: var(--ink);
  }
  .brand-square {
    width: 84px;
    height: 84px;
    background: var(--blue-light);
  }
  .headline {
    position: absolute;
    right: 84px;
    top: 160px;
    text-align: right;
    font-family: "Oswald", "Arial Narrow", sans-serif;
    font-weight: 600;
    font-size: 78px;
    line-height: 84px;
    letter-spacing: 6px;
    color: var(--blue-mid);
  }
  .subline {
    position: absolute;
    right: 82px;
    top: 320px;
    font-size: 28px;
    font-weight: 500;
    letter-spacing: 3.4px;
    color: var(--ink);
  }
  .cta {
    position: absolute;
    left: 735px;
    top: 450px;
    width: 465px;
    height: 72px;
    background: var(--blue-light);
    box-shadow: 0 8px 0 var(--cta-shadow);
    display: flex;
    align-items: center;
    padding-left: 34px;
    gap: 20px;
    color: var(--white);
    text-decoration: none;
    font-size: 38px;
    letter-spacing: 3px;
  }
  .cta-light { font-weight: 400; }
  .cta-bold { font-weight: 700; margin-left: -6px; }
  .cta-icon { width: 48px; height: 48px; }
  .web {
    position: absolute;
    left: 44px;
    top: 536px;
    display: flex;
    align-items: center;
    gap: 22px;
    color: var(--white);
    font-size: 20px;
    letter-spacing: 0.5px;
  }
  .web-icon { width: 90px; height: 56px; }
</style>
</head>
<body>
<main class="banner">
  <svg class="backdrop" viewBox="0 0 1200 628" aria-hidden="true">
    <polygon points="0,40 0,628 640,628" fill="var(--blue-deep)"/>
    <polygon points="0,40 480,628 640,628" fill="var(--blue-mid)" opacity="0.55"/>
    <polygon points="0,40 0,330 300,628 480,628" fill="var(--blue-light)" opacity="0.45"/>
    <polygon points="420,628 1200,400 1200,628" fill="var(--blue-navy)"/>
    <polygon points="560,628 1200,460 1200,628" fill="var(--blue-deep)"/>
  </svg>

  <svg class="coins" viewBox="0 0 620 500" role="img" aria-label="Three collectible coins: a gold bullion coin, a silver proof eagle and a dark antique silver dollar">
    <defs>
      <radialGradient id="gold" cx="40%" cy="35%" r="70%">
        <stop offset="0" stop-color="var(--gold-1)"/><stop offset="1" stop-color="var(--gold-2)"/>
      </radialGradient>
      <radialGradient id="silver" cx="45%" cy="40%" r="70%">
        <stop offset="0" stop-color="var(--silver-1)"/><stop offset="1" stop-color="var(--silver-2)"/>
      </radialGradient>
      <radialGradient id="bronze" cx="50%" cy="45%" r="65%">
        <stop offset="0" stop-color="var(--bronze-1)"/><stop offset="1" stop-color="var(--bronze-2)"/>
      </radialGradient>
    </defs>
    <circle cx="474" cy="134" r="132" fill="url(#bronze)"/>
    <circle cx="320" cy="198" r="138" fill="url(#silver)"/>
    <circle cx="130" cy="365" r="132" fill="url(#gold)"/>
  </svg>

  <div class="brand">
    <span class="brand-name">KESTRELBY</span>
    <span class="brand-square" aria-hidden="true"></span>
  </div>

  <h1 class="headline">SPECIALTY<br>INSURANCE</h1>
  <p class="subline">FOR YOUR COIN COLLECTION</p>

  <a class="cta" href="#">
    <span><span class="cta-light">GET</span> <span class="cta-bold">STARTED</span></span>
    <svg class="cta-icon" viewBox="0 0 48 48" aria-hidden="true">
      <circle cx="24" cy="24" r="21" fill="none" stroke="var(--white)" stroke-width="3"/>
      <polygon points="19,14 34,24 19,34" fill="var(--white)"/>
    </svg>
  </a>

  <div class="web">
    <svg class="web-icon" viewBox="0 0 90 56" aria-hidden="true">
      <rect x="2" y="6" width="76" height="36" rx="8" fill="none" stroke="var(--white)" stroke-width="3"/>
      <text x="10" y="30" fill="var(--white)" font-family="Montserrat, sans-serif" font-weight="700" font-size="15">www://</text>
      <polygon points="62,28 62,54 68,47 74,55 78,53 72,45 81,44" fill="var(--white)" stroke="var(--blue-deep)" stroke-width="1"/>
    </svg>
    <span class="web-address">www.kestrelby-ins.com</span>
  </div>
</main>
</body>
</html>
```